Design nice user interface for an IQ test website

I need you to design a modern user interface for IQ-test website. Questions and answers for the test are already known.

The test itself has all the questions in the form of an image where a portion of the image is cut off, and then the user has either 6 or 8 possible answers. The user needs to click one option to select his answer.

Proof of concept is here (you can find test questions there already):
https://vorpelin.org/projects/IQ-test/

I need only the design from you, no programming at all. The test questions are already given, you will not create your own questions/answers. Note that the images for test questions and answers (as shown at the URL) are not blue, they are transparent PNGs. So the background does not need to be blue.

While thinking about the design, consider adding nice progress bar (so user knows how many more questions to answer), and there needs to be also a time limit, which counts from 40:00 minutes down to zero.

Redesign for the actual questions/answer images is not required. If you decide to redesign the questions to make them nicer, you can do so, you may have higher chances to be selected as a winner, but keep in mind there are 60 questions in total, so it will be lot of additional work for you (feel free to suggest your idea).

Keep in mind that the design must be convertable to a "portrait mode" (eg. for devices where screen width is small)

Feel free to get as creative as you like.

So basically I would like to see at least 3 pages from you designed:
- some basic main page of the website with some lorem ipsum texts, and a "START TEST" button
- test page (where the test questions are displayed and answers are selected)
- a form page (after test is completed, user will enter name/email/age and click some button to get the test results emailed to him)

```html
<!DOCTYPE html>
<html lang="en">
<head>
<meta charset="utf-8">
<title>IQ Test Website — Web Interface Design</title>
<link rel="stylesheet" href="https://fonts.googleapis.com/css2?family=Inter:wght@400;500;600;700;800&display=swap">
<style>
:root{
  --board:#e5e5fa;
  --primary:#4a4de3;
  --primary-soft:#d9d9fb;
  --primary-pale:#eeeefd;
  --ink:#1d1d3b;
  --muted:#7b7d95;
  --line:#dcdce8;
  --card:#ffffff;
  --red:#f2544d;
  --green:#a9ea5c;
  --yellow:#ffcf3f;
  --peach:#fde3d6;
  --mint:#eef8df;
  --illus:#bfc0f4;
}
*{box-sizing:border-box;margin:0;padding:0}
html,body{width:1200px;height:1200px;overflow:hidden}
body{background:var(--board);font-family:'Inter',sans-serif;color:var(--ink);position:relative}

.board-title{position:absolute;left:132px;top:160px;font-size:86px;font-weight:700;letter-spacing:-1.5px;color:var(--primary);line-height:1}
.board-subtitle{position:absolute;left:134px;top:282px;font-size:34px;font-weight:400;color:var(--primary);letter-spacing:.5px}

.stage{position:absolute;left:0;top:0;width:1200px;height:1600px;transform:skewY(-8deg);transform-origin:0 0}
.screen{position:absolute;background:var(--card);border-radius:14px;overflow:hidden;box-shadow:0 10px 30px rgba(74,77,227,.08)}
.abs{position:absolute}

/* shared UI */
.brand-pill{position:absolute;display:flex;align-items:center;gap:6px;background:#fff;border-radius:6px;box-shadow:0 3px 10px rgba(40,40,90,.12);padding:0 10px;font-weight:700;color:var(--ink)}
.brand-mark{width:9px;height:9px;border-radius:2px;background:var(--primary)}
.nav-link{position:absolute;font-size:7px;color:var(--ink)}
.btn{position:absolute;display:flex;align-items:center;justify-content:center;gap:3px;border-radius:4px;font-weight:600;white-space:nowrap}
.btn-primary{background:var(--primary);color:#fff}
.btn-outline{background:#fff;color:var(--primary);border:1px solid var(--primary-soft)}
.tag{position:absolute;display:flex;flex-direction:column;align-items:center;justify-content:center;border-radius:4px;font-weight:800;color:var(--ink);line-height:1}
.tag small{font-size:.45em;font-weight:500;margin-bottom:2px}
.tag-red{background:var(--red);color:#fff}
.tag-green{background:var(--green)}
.tag-yellow{background:var(--yellow)}
.illustration{position:absolute;border-radius:45%}
.brain{background:radial-gradient(circle at 50% 45%,#cfd0f8 0%,var(--illus) 70%)}
.confetti{border-radius:40%;background:radial-gradient(circle at 40% 40%,#ffd76a 0%,#f78aa0 45%,rgba(110,120,240,.35) 75%,rgba(255,255,255,0) 100%)}
.lede{position:absolute;font-size:7px;line-height:11px;color:var(--muted)}
.heading{position:absolute;font-weight:800;color:var(--primary)}
.timer{position:absolute;display:flex;align-items:center;gap:4px;border:1px solid var(--line);border-radius:12px;font-size:8px;font-weight:600;padding:0 7px;height:18px;background:#fff}
.timer svg{width:9px;height:9px}
.left-chip{position:absolute;background:var(--yellow);border-radius:3px;font-size:6px;font-weight:600;padding:2px 4px}
.puzzle{position:absolute;border-radius:4px;background:linear-gradient(135deg,#f3f3f8,#e4e4ee);border:1px solid #c9c9d6}
.option{position:absolute;border:1px solid var(--line);border-radius:8px;background:#fff}
.option.is-selected{background:var(--primary-soft);border-color:var(--primary-soft)}
.option .shape{position:absolute;left:18%;top:16%;width:64%;height:50%;border-radius:3px;background:linear-gradient(135deg,#ececf3,#cfd0dc)}
.option .letter{position:absolute;left:0;right:0;bottom:4px;text-align:center;font-size:8px;color:var(--ink)}
.option.is-selected .letter{color:var(--primary);font-weight:600}
.cell{position:absolute;width:19px;height:19px;border:1px solid var(--line);border-radius:4px;font-size:7px;display:flex;align-items:center;justify-content:center;background:#fff}
.cell.is-current{background:var(--primary);color:#fff;border-color:var(--primary)}
.cell.is-done{background:var(--primary-soft);border-color:var(--primary-soft);color:var(--primary)}

.form-card{position:absolute;background:#fff;border-radius:10px;box-shadow:0 8px 24px rgba(40,40,110,.14);overflow:hidden}
.form-note{display:flex;align-items:center;gap:4px;background:var(--primary-soft);color:var(--primary);font-size:6px;padding:0 10px;height:22px}
.form-note i{width:7px;height:7px;border-radius:50%;background:var(--primary);display:inline-block}
.field{margin:12px 14px 0}
.field label{display:block;font-size:7px;font-weight:600;margin-bottom:6px}
.field span{display:block;font-size:6px;color:#b1b2c3;padding-bottom:4px;border-bottom:1px solid var(--line)}
</style>
</head>
<body>

<h1 class="board-title">IQ Test Website</h1>
<p class="board-subtitle">Web Interface Design</p>

<div class="stage">

  <!-- Desktop home -->
  <section class="screen home-desktop" style="left:7px;top:584px;width:543px;height:367px;background:linear-gradient(160deg,#fff 45%,var(--mint) 100%)">
    <div class="brand-pill" style="left:12px;top:28px;height:30px;font-size:9px"><span class="brand-mark"></span>Cortexa</div>
    <span class="nav-link" style="left:96px;top:40px">Home</span>
    <span class="nav-link" style="left:135px;top:40px">About Us</span>
    <span class="nav-link" style="left:188px;top:40px">FAQ</span>
    <span class="btn btn-primary" style="left:362px;top:20px;width:51px;height:21px;font-size:7px">Start Test</span>
    <span class="btn btn-outline" style="left:418px;top:20px;width:60px;height:21px;font-size:7px">How It Works</span>

    <h2 class="heading" style="left:28px;top:84px;font-size:20px">Know Your IQ Score</h2>
    <p class="lede" style="left:28px;top:116px;width:232px">Lorem ipsum dolor sit amet, consectetur adipiscing elit. Vivamus quis odio rhoncus, sodales ante vitae, pharetra lectus. Ut ac sem nec arcu rutrum molestie at quis eros. Fusce eros libero, gravida iaculis magna eu, aliquam congue eros. In suscipit massa a neque tincidunt, non vehicula ex molestie.</p>
    <p class="lede" style="left:28px;top:186px;width:232px">Sed in tortor a tortor ultrices lobortis. Duis pellentesque quis velit at lobortis. Pellentesque pharetra ac lacus eu aliquam. Fusce euismod purus erat, id porta nunc imperdiet in.</p>
    <span class="btn btn-primary" style="left:50px;top:262px;width:60px;height:23px;font-size:7px">Start Test ›</span>
    <span class="btn btn-outline" style="left:116px;top:260px;width:60px;height:23px;font-size:7px">How It Works</span>

    <div class="illustration brain" role="img" aria-label="Illustration of a purple brain" style="left:345px;top:105px;width:128px;height:98px"></div>
    <span class="tag tag-red" style="left:352px;top:95px;width:28px;height:18px;font-size:8px">97?</span>
    <span class="tag tag-green" style="left:336px;top:168px;width:52px;height:40px;font-size:15px"><small>Your IQ :</small>125?</span>
    <span class="tag tag-yellow" style="left:436px;top:162px;width:32px;height:20px;font-size:8px">112?</span>
  </section>

  <!-- Desktop result form -->
  <section class="screen result-desktop" style="left:571px;top:578px;width:596px;height:347px;background:radial-gradient(circle at 100% 100%,var(--peach) 0%,rgba(255,255,255,0) 45%),radial-gradient(circle at 0% 70%,#fdeee4 0%,rgba(255,255,255,0) 35%),#fff">
    <div class="brand-pill" style="left:62px;top:26px;height:26px;font-size:8px"><span class="brand-mark"></span>Cortexa</div>
    <span class="nav-link" style="left:150px;top:36px">Home</span>
    <span class="nav-link" style="left:190px;top:36px">About Us</span>
    <span class="nav-link" style="left:244px;top:36px">FAQ</span>
    <span class="btn btn-primary" style="left:416px;top:16px;width:50px;height:21px;font-size:7px">Start Test</span>
    <span class="btn btn-outline" style="left:472px;top:16px;width:60px;height:21px;font-size:7px">How It Works</span>

    <h2 class="abs" style="left:0;right:0;top:66px;text-align:center;font-size:22px;font-weight:800">Congratulations!</h2>
    <p class="abs" style="left:0;right:0;top:94px;text-align:center;font-size:7px;font-weight:600">You have completed the IQ test</p>

    <div class="illustration confetti" role="img" aria-label="Party popper with confetti" style="left:176px;top:200px;width:80px;height:72px"></div>
    <div class="illustration confetti" role="img" aria-label="Party popper with confetti" style="left:402px;top:122px;width:82px;height:80px"></div>

    <div class="form-card" style="left:240px;top:110px;width:198px;height:260px">
      <div class="form-note"><i></i>Your test result will be sent to your email</div>
      <div class="field"><label>Your Name</label><span>Alex Rowan</span></div>
      <div class="field"><label>Your Age</label><span>28</span></div>
      <div class="field"><label>Your Email</label><span>you@example.com</span></div>
      <span class="btn btn-primary" style="left:148px;top:162px;width:40px;height:20px;font-size:7px">Submit</span>
    </div>
  </section>

  <!-- Desktop test page -->
  <section class="screen test-desktop" style="left:13px;top:971px;width:600px;height:420px">
    <p class="abs" style="left:0;right:0;top:14px;text-align:center;font-size:7px;color:var(--muted)">Select the best replacement image.</p>
    <span class="timer" style="left:490px;top:22px"><svg viewBox="0 0 10 10"><circle cx="5" cy="5" r="4" fill="none" stroke="#1d1d3b" stroke-width="1"/><path d="M5 3v2.2l1.4 1" fill="none" stroke="#1d1d3b" stroke-width="1"/></svg>29:58</span>
    <span class="btn btn-outline" style="left:68px;top:34px;width:48px;height:19px;font-size:7px;color:var(--ink)">◁ Leave</span>

    <div class="puzzle" role="img" aria-label="Question image: woven line pattern with a cut-out piece" style="left:112px;top:66px;width:222px;height:130px"></div>

    <div class="abs" style="left:360px;top:38px;width:200px;height:150px;border:1px solid var(--line);border-radius:8px">
      <span class="abs" style="left:10px;top:14px;font-size:7px">Question <b style="font-size:9px">26</b>/60</span>
      <span class="left-chip" style="left:162px;top:12px">34 left</span>
      <span class="cell" style="left:12px;top:34px">25</span>
      <span class="cell is-current" style="left:36px;top:34px">26</span>
      <span class="cell is-done" style="left:60px;top:34px">27</span>
      <span class="cell" style="left:84px;top:34px">28</span>
      <span class="cell" style="left:108px;top:34px">29</span>
      <span class="cell" style="left:132px;top:34px">30</span>
      <span class="cell" style="left:12px;top:58px">31</span>
      <span class="cell" style="left:36px;top:58px">32</span>
      <span class="cell" style="left:60px;top:58px">33</span>
      <span class="cell" style="left:84px;top:58px">34</span>
      <span class="cell is-done" style="left:108px;top:58px">35</span>
      <span class="cell" style="left:132px;top:58px">36</span>
      <span class="cell" style="left:12px;top:82px">37</span>
      <span class="cell" style="left:36px;top:82px">38</span>
      <span class="cell" style="left:60px;top:82px">39</span>
      <span class="cell" style="left:84px;top:82px">40</span>
      <span class="cell" style="left:108px;top:82px">41</span>
      <span class="cell" style="left:132px;top:82px">42</span>
      <span class="abs" style="left:176px;top:34px;width:3px;height:56px;border-radius:2px;background:var(--line)"></span>
      <span class="abs" style="left:176px;top:34px;width:3px;height:24px;border-radius:2px;background:var(--ink)"></span>
      <span class="btn btn-outline" style="left:10px;top:116px;width:82px;height:20px;font-size:7px;color:var(--ink)">← Previous</span>
      <span class="btn btn-primary" style="left:98px;top:116px;width:90px;height:20px;font-size:7px">Next →</span>
    </div>

    <div class="option is-selected" style="left:102px;top:212px;width:70px;height:62px"><span class="shape" role="img" aria-label="Answer piece a"></span><span class="letter">a</span></div>
    <div class="option" style="left:180px;top:208px;width:70px;height:62px"><span class="shape" role="img" aria-label="Answer piece b"></span><span class="letter">b</span></div>
    <div class="option" style="left:258px;top:204px;width:70px;height:62px"><span class="shape" role="img" aria-label="Answer piece c"></span><span class="letter">c</span></div>
    <div class="option" style="left:336px;top:200px;width:70px;height:62px"><span class="shape" role="img" aria-label="Answer piece d"></span><span class="letter">d</span></div>
    <div class="option" style="left:414px;top:196px;width:70px;height:62px"><span class="shape" role="img" aria-label="Answer piece e"></span><span class="letter">e</span></div>
    <div class="option" style="left:492px;top:192px;width:70px;height:62px"><span class="shape" role="img" aria-label="Answer piece f"></span><span class="letter">f</span></div>
  </section>

  <!-- Mobile home -->
  <section class="screen home-mobile" style="left:633px;top:948px;width:193px;height:400px;background:linear-gradient(170deg,#fff 55%,var(--mint) 100%)">
    <div class="brand-pill" style="left:16px;top:18px;width:161px;height:32px;font-size:10px"><span class="brand-mark"></span>Cortexa
      <svg class="abs" style="right:10px;top:11px" width="10" height="9" viewBox="0 0 10 9"><path d="M0 1h10M0 4.5h10M0 8h10" stroke="#1d1d3b" stroke-width="1.2"/></svg>
    </div>
    <div class="illustration brain" role="img" aria-label="Illustration of a purple brain" style="left:66px;top:66px;width:92px;height:72px"></div>
    <span class="tag tag-red" style="left:72px;top:60px;width:24px;height:16px;font-size:8px">97?</span>
    <span class="tag tag-green" style="left:58px;top:120px;width:48px;height:38px;font-size:14px"><small>Your IQ :</small>112?</span>
    <span class="tag tag-yellow" style="left:130px;top:114px;width:30px;height:20px;font-size:8px">125?</span>
    <h2 class="heading" style="left:20px;top:188px;width:140px;font-size:16px;line-height:20px;color:var(--ink)">Know Your IQ Score</h2>
    <p class="lede" style="left:20px;top:238px;width:156px">Lorem ipsum dolor sit amet, consectetur adipiscing elit. Vivamus quis odio rhoncus, sodales ante vitae, pharetra lectus. Ut ac sem nec arcu rutrum molestie at quis eros. Fusce eros libero, gravida iaculis magna eu, aliquam congue eros. In suscipit massa a neque tincidunt, non vehicula ex molestie. Nullam nec semper lorem sed.</p>
    <span class="btn btn-primary" style="left:20px;top:340px;width:156px;height:24px;font-size:8px">Start Test ›</span>
  </section>

  <!-- Mobile test page -->
  <section class="screen test-mobile" style="left:853px;top:948px;width:193px;height:400px">
    <span class="btn btn-outline" style="left:12px;top:16px;width:18px;height:18px;font-size:8px;color:var(--ink)">◁</span>
    <span class="abs" style="left:38px;top:20px;font-size:10px;font-weight:700">26<span style="font-size:7px;font-weight:400">/60</span></span>
    <span class="left-chip" style="left:74px;top:20px">34 left</span>
    <span class="timer" style="left:128px;top:16px">
      <svg viewBox="0 0 10 10"><circle cx="5" cy="5" r="4" fill="none" stroke="#1d1d3b" stroke-width="1"/><path d="M5 3v2.2l1.4 1" fill="none" stroke="#1d1d3b" stroke-width="1"/></svg>29:58</span>
    <div class="abs" style="left:10px;top:44px;width:176px;height:32px;border:1px solid var(--line);border-radius:8px"></div>
    <span class="cell is-done" style="left:6px;top:50px">24</span>
    <span class="cell" style="left:30px;top:50px">25</span>
    <span class="cell is-current" style="left:54px;top:50px">26</span>
    <span class="cell is-done" style="left:78px;top:50px">27</span>
    <span class="cell" style="left:102px;top:50px">28</span>
    <span class="cell" style="left:126px;top:50px">29</span>
    <span class="cell" style="left:150px;top:50px">30</span>
    <div class="puzzle" role="img" aria-label="Question image: woven line pattern with a cut-out piece" style="left:34px;top:96px;width:140px;height:104px"></div>
    <div class="option is-selected" style="left:30px;top:214px;width:46px;height:42px"><span class="shape" role="img" aria-label="Answer piece a"></span><span class="letter">a</span></div>
    <div class="option" style="left:84px;top:214px;width:46px;height:42px"><span class="shape" role="img" aria-label="Answer piece b"></span><span class="letter">b</span></div>
    <div class="option" style="left:138px;top:214px;width:46px;height:42px"><span class="shape" role="img" aria-label="Answer piece c"></span><span class="letter">c</span></div>
    <div class="option" style="left:30px;top:264px;width:46px;height:42px"><span class="shape" role="img" aria-label="Answer piece d"></span><span class="letter">d</span></div>
    <div class="option" style="left:84px;top:264px;width:46px;height:42px"><span class="shape" role="img" aria-label="Answer piece e"></span><span class="letter">e</span></div>
    <div class="option" style="left:138px;top:264px;width:46px;height:42px"><span class="shape" role="img" aria-label="Answer piece f"></span><span class="letter">f</span></div>
    <span class="btn btn-outline" style="left:30px;top:330px;width:62px;height:24px;font-size:8px;color:var(--ink)">←</span>
    <span class="btn btn-primary" style="left:100px;top:324px;width:84px;height:26px;font-size:8px">Next →</span>
  </section>

  <!-- Mobile result form -->
  <section class="screen result-mobile" style="left:1073px;top:948px;width:193px;height:400px;background:linear-gradient(180deg,#fff 60%,#fdf0e9 100%)">
    <div class="brand-pill" style="left:14px;top:16px;width:170px;height:30px;font-size:10px"><span class="brand-mark"></span>Cortexa</div>
    <h2 class="abs" style="left:26px;top:62px;font-size:17px;font-weight:800;white-space:nowrap">Congratulations!</h2>
    <p class="abs" style="left:26px;top:84px;font-size:6px;font-weight:600;white-space:nowrap">You have completed the IQ test</p>
    <div class="illustration confetti" role="img" aria-label="Party popper with confetti" style="left:46px;top:100px;width:70px;height:54px"></div>
    <div class="form-card" style="left:32px;top:166px;width:160px;height:230px">
      <div class="form-note"><i></i>Your test result will be sent</div>
      <div class="field"><label>Your Name</label><span>Alex Rowan</span></div>
      <div class="field"><label>Your Age</label><span>28</span></div>
      <div class="field"><label>Your Email</label><span>you@example.com</span></div>
      <span class="btn btn-primary" style="left:14px;top:182px;width:132px;height:22px;font-size:7px">Submit</span>
    </div>
  </section>

</div>
</body>
</html>
```